Home Design company focused on remodel and enhancement of kitchens and bathroorms

I already have a logo designed by ArtHarbor, I now need a design for my business cards.
The company is in the remodeling and enhancement industry for homes, focusing on kitchens and bathrooms, however, we can remodel or enhance every room in a home, an office space, etc.

The company's name is VELMOR HOME DESIGN, LLC

We'll focus on clients in the Rio Grande Valley, Texas. Primarily McAllen, Edinburg, Pharr, Mission, Brownsville and South Padre Island.

The design on the business card should transmit reliability, professionalism anda bit of upscale design.

The logo is in black and white, and would like to keep it that way.

The information that needs to be printed in the business cards is:
Company's name: Velmor Home Design
Company's Logo (attached)
My name: Noel Bramwit
Address, phone and email:
2715 N Parkline Road, Ste 348
Corvelle, TX 79990
(555) 555 0187
nbramwit@velmordesign.example
Website: velmordesign.example

```html
<!DOCTYPE html>
<html lang="en">
<head>
<meta charset="utf-8">
<title>Velmor Home Design – Business Cards</title>
<link rel="stylesheet" href="https://fonts.googleapis.com/css2?family=Open+Sans:wght@400;700&display=swap">
<style>
  :root {
    --backdrop: #8f9090;
    --card-white: #e8e8ea;
    --card-black: #000000;
    --ink-strong: #0c0c0c;
    --ink-soft: #4a4a4a;
    --mark-white: #ececec;
  }
  * { box-sizing: border-box; margin: 0; padding: 0; }
  html, body {
    width: 1200px; height: 1200px; overflow: hidden;
    background: var(--backdrop);
    font-family: "Open Sans", sans-serif;
  }
  .canvas { position: relative; width: 1200px; height: 1200px; }

  .card {
    position: absolute; left: 209px; width: 796px; height: 440px;
    overflow: hidden;
  }
  .card--front { top: 99px; background: var(--card-white); }
  .card--back { top: 634px; background: var(--card-black); }

  /* Front */
  .brand-band {
    position: absolute; left: 0; top: 0; width: 161px; height: 100%;
    background: var(--card-black);
  }
  .brand-band__mark {
    position: absolute; left: 50%; top: 50%;
    display: flex; align-items: center; gap: 28px;
    transform: translate(-50%, -50%) rotate(-90deg);
    white-space: nowrap;
  }
  .brand-square { width: 62px; height: 62px; background: var(--mark-white); flex: none; }
  .brand-name {
    color: var(--mark-white); font-weight: 400;
    text-transform: uppercase; letter-spacing: 0.45em;
    font-size: 15px; line-height: 1.45;
  }

  .contact {
    position: absolute; left: 325px; top: 104px;
    color: var(--ink-soft);
  }
  .contact__name {
    font-weight: 700; font-size: 35px; line-height: 1;
    color: var(--ink-strong); letter-spacing: -0.005em;
  }
  .contact__role { font-size: 19px; margin-top: 8px; line-height: 1.3; }
  .contact__address { font-size: 19px; line-height: 27px; margin-top: 10px; }
  .contact__list { list-style: none; margin-top: 8px; }
  .contact__item {
    display: flex; align-items: center; gap: 9px;
    font-size: 19px; line-height: 28px;
  }
  .contact__icon { width: 17px; height: 17px; flex: none; fill: var(--ink-strong); }

  /* Back */
  .back-lockup {
    position: absolute; left: 50%; top: 50%;
    transform: translate(-50%, -50%);
    display: flex; align-items: center; gap: 44px;
  }
  .back-lockup .brand-square { width: 104px; height: 104px; }
  .back-lockup .brand-name { font-size: 38px; letter-spacing: 0.3em; line-height: 1.1; }
</style>
</head>
<body>
<div class="canvas">

  <section class="card card--front">
    <div class="brand-band">
      <div class="brand-band__mark">
        <div class="brand-square"></div>
        <div class="brand-name">Velmor<br>Home<br>Design</div>
      </div>
    </div>

    <div class="contact">
      <h1 class="contact__name">Noel Bramwit</h1>
      <p class="contact__role">Founder &amp; CEO</p>
      <p class="contact__address">2715 N Parkline Road, Ste 348<br>Corvelle, TX 79990</p>
      <ul class="contact__list">
        <li class="contact__item">
          <svg class="contact__icon" viewBox="0 0 24 24" aria-hidden="true"><path d="M6.6 10.8a15.1 15.1 0 0 0 6.6 6.6l2.2-2.2a1 1 0 0 1 1-.25 11.4 11.4 0 0 0 3.6.57 1 1 0 0 1 1 1V20a1 1 0 0 1-1 1A17 17 0 0 1 3 4a1 1 0 0 1 1-1h3.5a1 1 0 0 1 1 1c0 1.25.2 2.45.57 3.57a1 1 0 0 1-.25 1z"/></svg>
          <span>(555) 555 0187</span>
        </li>
        <li class="contact__item">
          <svg class="contact__icon" viewBox="0 0 24 24" aria-hidden="true"><path d="M2 5h20v2l-10 6L2 7z M2 9l10 6 10-6v10H2z"/></svg>
          <span>nbramwit@velmordesign.example</span>
        </li>
        <li class="contact__item">
          <svg class="contact__icon" viewBox="0 0 24 24" aria-hidden="true"><circle cx="12" cy="12" r="10"/><path d="M8 6c2 1 2 3 1 4s-3 1-3 3 2 2 3 4M15 5c-1 2 1 3 2 3s2 2 1 4-2 1-3 3 1 3 0 4" stroke="#e8e8ea" stroke-width="1.6" fill="none"/></svg>
          <span>velmordesign.example</span>
        </li>
      </ul>
    </div>
  </section>

  <section class="card card--back">
    <div class="back-lockup">
      <div class="brand-square"></div>
      <div class="brand-name">Velmor<br>Home<br>Design</div>
    </div>
  </section>

</div>
</body>
</html>
```